Website for SEO Agency That Serves Family Law Attorneys

I need a design for a website that is clean, conversion focused and professional. The site should have a parallax feel and look very up-to-date. This homepage looks a lot like what I will need https://trelvaro.com/. I will also need a professional logo that is recognizable and tells users a little about how we do SEO just by looking at it.

```html
<!DOCTYPE html>
<html lang="en">
<head>
<meta charset="utf-8">
<title>Veralune – SEO for Family Law Attorneys</title>
<link href="https://fonts.googleapis.com/css2?family=Quicksand:wght@500;600&family=Lato:wght@400;700&display=swap" rel="stylesheet">
<style>
:root{
  --brand:#2b8ad8;
  --brand-dark:#2479c2;
  --text:#555a60;
  --heading:#2b8ad8;
  --light-bg:#efefef;
  --field-bg:#ececec;
  --field-border:#d4d4d4;
  --footer-bg:#2a2a2a;
  --footer-text:#bdbdbd;
  --white:#ffffff;
}
*{box-sizing:border-box;margin:0;padding:0}
html,body{width:1200px;height:2898px;overflow:hidden;background:var(--white)}
body{position:relative;font-family:'Lato',sans-serif;color:var(--text)}
.abs{position:absolute}
.btn{position:absolute;display:flex;align-items:center;justify-content:center;background:var(--brand);color:var(--white);font-family:'Lato',sans-serif;font-size:14px;letter-spacing:.2px;text-transform:uppercase}
.section-title{position:absolute;left:0;width:1200px;text-align:center;font-family:'Quicksand',sans-serif;font-weight:500;font-size:34px;color:var(--heading)}

/* header */
.site-header{position:absolute;left:0;top:0;width:1200px;height:79px;background:var(--white)}
.brand-name{position:absolute;left:142px;top:16px;font-family:'Quicksand',sans-serif;font-weight:600;font-size:39px;color:var(--brand);line-height:1}
.main-nav{position:absolute;right:144px;top:35px;display:flex;gap:36px;font-size:13px;text-transform:uppercase;color:#555}
.main-nav .active{color:var(--brand)}

/* hero */
.hero{position:absolute;left:0;top:79px;width:1200px;height:535px;background:linear-gradient(90deg,#b9c3cf 0%,#8c97a4 25%,#3b3f47 45%,#2d3037 62%,#6f7681 85%,#a9b0bb 100%)}
.hero-title{position:absolute;right:145px;top:216px;text-align:right;font-family:'Quicksand',sans-serif;font-weight:500;font-size:40px;line-height:48px;color:var(--white)}
.hero .btn{left:928px;top:324px;width:127px;height:40px;font-size:16px;font-weight:700}
.chev{position:absolute}

/* welcome */
.welcome-text{position:absolute;left:144px;top:735px;width:912px;text-align:center;font-size:14px;line-height:24px}

/* seo band */
.seo-band{position:absolute;left:0;top:965px;width:1200px;height:440px;background:linear-gradient(120deg,#3b96dc 0%,#2f88d0 55%,#4a9ee0 100%)}
.seo-image{position:absolute;left:144px;top:81px;width:280px;height:279px;background:linear-gradient(160deg,#d9c9ad 0%,#b79d78 60%,#6e5a45 100%)}
.seo-title{position:absolute;left:449px;top:112px;font-family:'Quicksand',sans-serif;font-weight:500;font-size:34px;color:var(--white)}
.seo-text{position:absolute;left:449px;top:163px;width:612px;font-size:14px;line-height:24px;color:var(--white)}
.seo-band .btn{left:449px;top:280px;width:111px;height:41px;background:var(--white);color:var(--brand)}

/* reviews */
.review-card{position:absolute;top:1533px;width:296px;height:232px;background:var(--light-bg)}
.review-card svg.quote{position:absolute;left:129px;top:32px}
.review-text{position:absolute;left:22px;top:74px;width:252px;text-align:center;font-size:14px;line-height:22.5px;color:#555}
.avatar{position:absolute;top:1734px;width:64px;height:64px;border-radius:50%;border:2px solid #ddd;background:linear-gradient(180deg,#9a8370,#e2cdb9)}
.reviewer{position:absolute;top:1802px;width:296px;text-align:center;font-size:14px;color:#333}
.dot{position:absolute;top:1842px;width:12px;height:12px;border-radius:50%;background:#d8d8d8}
.dot.current{background:#666}

/* cta */
.cta-band{position:absolute;left:0;top:1934px;width:1200px;height:439px;background:linear-gradient(100deg,#3b2a20 0%,#4a3628 40%,#5b5550 62%,#2a2a2c 80%,#1f1f21 100%)}
.cta-title{position:absolute;left:0;top:142px;width:1200px;text-align:center;font-family:'Quicksand',sans-serif;font-weight:500;font-size:34px;line-height:42px;color:var(--white)}
.cta-band .btn{left:544px;top:242px;width:112px;height:42px}

/* contact */
.field{position:absolute;background:var(--field-bg);border:1px solid var(--field-border);font-size:12px;color:#888;padding:14px 15px}

/* footer */
.site-footer{position:absolute;left:0;top:2802px;width:1200px;height:96px;background:var(--footer-bg);font-size:11px;color:var(--footer-text)}
.footer-links{position:absolute;left:144px;top:25px}
.copyright{position:absolute;left:144px;top:55px}
.footer-info{position:absolute;right:253px;text-align:right}
.social{position:absolute;top:17px;width:32px;height:32px;border-radius:50%;background:#6a6a6a}
</style>
</head>
<body>

<header class="site-header">
  <div class="brand-name">Veralune</div>
  <nav class="main-nav">
    <span class="active">Home</span><span>About Us</span><span>Services</span><span>Blog</span><span>Contact Us</span>
  </nav>
</header>

<section class="hero" role="img" aria-label="Photo of a businessman working on a laptop with a coffee cup on a city street">
  <svg class="chev" style="left:54px;top:250px" width="20" height="32" viewBox="0 0 20 32"><path d="M16 3 L4 16 L16 29" fill="none" stroke="#fff" stroke-width="4"/></svg>
  <svg class="chev" style="left:1126px;top:250px" width="20" height="32" viewBox="0 0 20 32"><path d="M4 3 L16 16 L4 29" fill="none" stroke="#fff" stroke-width="4"/></svg>
  <h1 class="hero-title">Etiam Fermentum<br>Ullamcorper</h1>
  <div class="btn">Contact Us</div>
</section>

<h2 class="section-title" style="top:685px">Welcome to Veralune</h2>
<p class="welcome-text">Aenean facilisis tincidunt lectus, id dictum nisi luctus eget. Vivamus efficitur ex condimentum, malesuada eros eget, feugiat nibh. Sed tellus ex, imperdiet eget gravida sit amet, volutpat eget turpis. In nec ultricies est. Etiam mattis augue vehicula odio posuere, sit amet tempus lectus luctus. Etiam vel massa elementum, bibendum tellus venenatis, feugiat massa. Curabitur venenatis lacinia ornare. Cras sollicitudin cursus dui eu placerat. Quisque aliquet ex nec est vestibulum pulvinar. Pellentesque convallis molestie enim sit amet efficitur.</p>
<div class="btn" style="left:544px;top:843px;width:112px;height:42px">Read More</div>

<section class="seo-band">
  <div class="seo-image" role="img" aria-label="Photo of wooden blocks spelling SEO with marketing icons"></div>
  <h2 class="seo-title">SEO Agency for Family Law Attorneys</h2>
  <p class="seo-text">Vivamus eleifend vitae nulla vel malesuada. In ac malesuada lacus, et consectetur ante. Fusce vitae lectus sit amet mi pulvinar maximus. Aenean placerat, nibh vel accumsan aliquet, magna nibh accumsan nibh, ac tempus nunc ipsum ac tellus. Cras augue magna, placerat eget nulla non, congue suscipit neque. Phasellus nisl est, condimentum vitae faucibus.</p>
  <div class="btn">Read More</div>
</section>

<h2 class="section-title" style="top:1477px">Reviews</h2>
<svg class="chev" style="left:60px;top:1638px" width="14" height="24" viewBox="0 0 14 24"><path d="M12 2 L3 12 L12 22" fill="none" stroke="#666" stroke-width="3"/></svg>
<svg class="chev" style="left:1121px;top:1638px" width="14" height="24" viewBox="0 0 14 24"><path d="M2 2 L11 12 L2 22" fill="none" stroke="#666" stroke-width="3"/></svg>

<article class="review-card" style="left:144px">
  <svg class="quote" width="38" height="32" viewBox="0 0 38 32"><g fill="#c4c4c4"><path d="M0 14 Q0 2 14 0 L14 6 Q7 7 7 13 L16 13 L16 32 L0 32Z"/><path d="M20 14 Q20 2 34 0 L34 6 Q27 7 27 13 L36 13 L36 32 L20 32Z"/></g></svg>
  <p class="review-text">Aenean facilisis tincidunt lectus, id dictum nisi luctus eget. Vivamus efficitur ex condimentum, malesuada eros eget, feugiat nibh. Sed tellus ex, imperdiet eget gravida sit amet.</p>
</article>
<article class="review-card" style="left:452px">
  <svg class="quote" width="38" height="32" viewBox="0 0 38 32"><g fill="#c4c4c4"><path d="M0 14 Q0 2 14 0 L14 6 Q7 7 7 13 L16 13 L16 32 L0 32Z"/><path d="M20 14 Q20 2 34 0 L34 6 Q27 7 27 13 L36 13 L36 32 L20 32Z"/></g></svg>
  <p class="review-text">Donec augue odio, varius quis sem at, pretium malesuada sapien. In pellen-tesque sem ultricies lorem molestie, eget elementum urna ornare. Quisque tincidunt est a ultricies.</p>
</article>
<article class="review-card" style="left:760px">
  <svg class="quote" width="38" height="32" viewBox="0 0 38 32"><g fill="#c4c4c4"><path d="M0 14 Q0 2 14 0 L14 6 Q7 7 7 13 L16 13 L16 32 L0 32Z"/><path d="M20 14 Q20 2 34 0 L34 6 Q27 7 27 13 L36 13 L36 32 L20 32Z"/></g></svg>
  <p class="review-text">Suspendisse sed nisl sit amet ex semper eleifend. Ut at eleifend magna. Vivamus malesuada mauris nulla, sed commodo sapien gravida sit amet. Sed dictum purus imperdiet.</p>
</article>
<div class="avatar" style="left:260px" role="img" aria-label="Portrait photo of reviewer Marc Deller"></div>
<div class="avatar" style="left:568px" role="img" aria-label="Portrait photo of reviewer Tessa"></div>
<div class="avatar" style="left:876px" role="img" aria-label="Portrait photo of reviewer Oliver"></div>
<div class="reviewer" style="left:144px">Marc Deller</div>
<div class="reviewer" style="left:452px">Tessa</div>
<div class="reviewer" style="left:760px">Oliver</div>
<span class="dot current" style="left:557px"></span>
<span class="dot" style="left:581px"></span>
<span class="dot" style="left:605px"></span>
<span class="dot" style="left:629px"></span>

<section class="cta-band" role="img" aria-label="Photo of a laptop keyboard on a dark wooden desk">
  <h2 class="cta-title">Etiam mattis augue vehicula odio posuere<br>sit amet tempus lectus luctus.</h2>
  <div class="btn">Read More</div>
</section>

<h2 class="section-title" style="top:2444px">Contact Us</h2>
<div class="field" style="left:144px;top:2503px;width:297px;height:41px">Name</div>
<div class="field" style="left:451px;top:2503px;width:297px;height:41px">Email</div>
<div class="field" style="left:758px;top:2503px;width:297px;height:41px">Phone</div>
<div class="field" style="left:144px;top:2557px;width:911px;height:96px">Message</div>
<div class="btn" style="left:544px;top:2680px;width:112px;height:41px">Submit</div>

<footer class="site-footer">
  <div class="footer-links">Home &nbsp;|&nbsp; About Us &nbsp;|&nbsp; Services &nbsp;|&nbsp; Blog &nbsp;|&nbsp; Contact Us</div>
  <div class="copyright">Copyright &copy; 2019 &nbsp;Veralune. &nbsp;All rights reserved.</div>
  <div class="footer-info" style="top:29px">
    <svg width="8" height="11" viewBox="0 0 8 11" style="vertical-align:-1px"><path d="M4 0 A4 4 0 0 1 8 4 Q8 6 4 11 Q0 6 0 4 A4 4 0 0 1 4 0Z" fill="#bdbdbd"/></svg>
    &nbsp;24 Building name, Street name, City Zipcode</div>
  <div class="footer-info" style="top:50px">
    <svg width="9" height="9" viewBox="0 0 9 9" style="vertical-align:-1px"><path d="M1 0 L3 0 L4 2.5 L2.8 3.5 Q4 6 5.5 6.2 L6.5 5 L9 6 L9 8 Q8 9 6.5 9 Q1 7 0 2 Q0 1 1 0Z" fill="#bdbdbd"/></svg>
    &nbsp;555 013 2270 &nbsp;&nbsp;|&nbsp;&nbsp;
    <svg width="10" height="8" viewBox="0 0 10 8" style="vertical-align:0"><rect width="10" height="8" fill="#bdbdbd"/><path d="M0 0 L5 4 L10 0" fill="none" stroke="#2a2a2a" stroke-width="1"/></svg>
    info@veralune.com</div>
  <span class="social" style="left:974px"></span>
  <span class="social" style="left:1021px"></span>
</footer>

</body>
</html>
```